Kelvar Lease-Plan sheds company needs new coded front end web page

Kelvar Lease provides a rent-to-own financing option to storage building dealers in the southeast U.S. We need a redesign of Kelvar Lease's front end web site.

Current site is https://www.kelvarlease.example/

I'm looking to get a coded (HTML & CSS) single page design. I am a PHP developer and looking to outsource the design of the front end of the site. You don't have to make anything work beyond HTML and CSS. I would like the layout to be done in Bootstrap and as such the CSS would already be done. You would just have to add your supplemental CSS for whatever background, colors, fonts, or custom elements that need to be styled.

The client's website does not have a whole lot of content, as you can see if you visit the page, so I'd like to turn the current front-end with multiple pages into a single page. Most of the content is quite short and I'd like an artful way to present it. I'd like to actually remove the menu at the top.

See this site for examples of Bootstrap layouts: https://themevault.example/themes/business?branch=3.x

If all goes well with this project, we would like to continue to work with the designer in the near future on some other similar projects.
Updates

I have updated the brief for single page design clarification.

The About Us page is a duplicate of the home page, so you can ignore that. The Rental Programs offered are actually 24, 36, 48, and 60. The FAQs page we will probably link to a modal window, so don't worry about its content; we just need a way to provide the link to it. The contact page info could use some nice styling. The Dealer Login page should become a single button like the Customer Payments at the top.

Industry/Entity Type

Building

Font styles to use
Sans Serif

Colors

Designer to choose colors to be used in the design.

Requirements
Must have
• The new design should be marked up with Bootstrap 3. It should be a responsive layout. The HTML, CSS, and any image assets should be provided. A PSD or other design file is not required, but we'll certainly take it if you made one anyway.

Clean, simple design.
Nice to have
• Some stock photography may help to explain in a glance what Kelvar Lease does. Some keywords to look for in stock photos: storage buildings, storage sheds, backyard storage, rent-to-own, barns. Note that you don't need to purchase the stock photos. Just use watermarked placeholders in your layout.

```html
<!DOCTYPE html>
<html lang="en">
<head>
<meta charset="utf-8">
<title>Kelvar Lease – Rent to Own Storage Buildings</title>
<link rel="stylesheet" href="https://fonts.googleapis.com/css2?family=Open+Sans:wght@300;400;600;700&family=Roboto+Condensed:wght@400;700&display=swap">
<style>
:root{
  --navy:#0c2d5a;
  --orange:#f5892a;
  --orange-deep:#ef7a18;
  --light:#f4f4f4;
  --white:#ffffff;
  --ink:#2b2b2b;
  --muted:#777;
  --dark:#2f2f2f;
  --black:#1b1b1b;
}
*{box-sizing:border-box;margin:0;padding:0}
html,body{width:1200px;height:3485px;overflow:hidden}
body{font-family:"Open Sans",Arial,sans-serif;color:var(--ink);background:var(--white)}
.title{font-family:"Roboto Condensed",Arial,sans-serif;font-weight:700;font-size:28px;text-transform:uppercase;text-align:center;letter-spacing:.3px}
.rule{width:80px;height:3px;margin:14px auto 0}
p{font-size:14px;line-height:22px}

/* header */
.site-header{height:70px;position:relative;background:var(--white);border-bottom:1px solid #e5e5e5}
.brand{position:absolute;left:155px;top:18px;font-family:"Roboto Condensed",Arial,sans-serif;font-weight:700;font-size:26px;color:var(--navy);display:flex;align-items:center;gap:8px}
.brand-dot{width:14px;height:14px;background:var(--orange);border-radius:50%}
.nav{position:absolute;left:355px;top:0;display:flex;height:70px}
.nav a{display:flex;align-items:center;padding:0 18px;font-size:13px;color:#666;text-decoration:none;border-right:1px solid #eee}
.nav a.active{background:#f3f3f3;color:#333;border-bottom:3px solid var(--orange)}
.nav a.btn-login{background:var(--orange);color:#fff;font-weight:600;border:0;margin-left:12px}
.nav a.btn-pay{background:var(--navy);color:#fff;font-weight:600;border:0}

/* hero */
.hero{height:510px;position:relative;background:linear-gradient(180deg,#8fb6e0 0%,#c9dcef 45%,#d9b27a 60%,#b88a4d 80%,#6d8a48 100%)}
.hero-tag{position:absolute;top:235px;left:0;right:0;text-align:center;font-family:"Roboto Condensed",Arial,sans-serif;font-weight:700;font-size:38px;line-height:44px}
.hero-tag span{display:inline-block;padding:0 14px;color:#fff}
.hero-tag .l1{background:var(--navy)}
.hero-tag .l2{background:var(--orange)}

/* welcome / about */
.welcome{height:420px;background:var(--light);padding-top:70px;text-align:center}
.welcome .title,.about .title{color:var(--navy)}
.welcome .rule,.about .rule{background:var(--navy)}
.copy{width:690px;margin:50px auto 0;color:#444}
.copy p+p{margin-top:20px}
.badge-photo{position:absolute;left:540px;top:940px;width:120px;height:120px;border-radius:50%;border:5px solid #fff;box-shadow:0 0 0 1px #ddd;background:linear-gradient(160deg,#a4c2dc 0%,#8a7a66 50%,#7a3a2e 70%,#6f8a4c 100%)}
.about{height:430px;padding-top:123px;text-align:center;background:var(--white)}
.about .copy{margin-top:58px}

/* rentals */
.rentals{height:525px;background:linear-gradient(135deg,var(--orange) 0%,var(--orange-deep) 100%);color:#fff;text-align:center;padding-top:56px}
.rentals .rule{background:#fff}
.terms-label{font-size:24px;margin-top:46px}
.terms{display:flex;justify-content:center;gap:40px;margin-top:38px}
.term{width:115px}
.term-ring{width:115px;height:115px;border-radius:50%;border:6px solid #fff;display:flex;align-items:center;justify-content:center}
.term-ring span{width:89px;height:89px;border-radius:50%;background:#f5f0ea;color:var(--orange);font-size:34px;display:flex;align-items:center;justify-content:center}
.term-unit{font-size:17px;margin-top:10px}
.rentals p{width:880px;margin:42px auto 0;font-size:14.5px}

/* faq */
.faq{height:450px;background:var(--navy);color:#fff;text-align:center;padding-top:56px}
.faq .rule{width:170px;background:#fff}
.faq-sub{font-size:24px;margin-top:32px}
.faq-item{margin-top:20px}
.faq-item h3{font-size:15px;font-weight:700}
.faq-item p{width:560px;margin:4px auto 0;font-size:13px;line-height:20px}
.btn-more{display:inline-block;margin-top:22px;background:#fff;color:var(--navy);font-weight:700;font-size:14px;padding:3px 16px;border-radius:2px;text-decoration:none}

/* contact */
.contact{height:975px;background:var(--dark);color:#ddd;position:relative;padding-top:52px}
.contact .title{color:#fff}
.contact .rule{background:#fff}
.col{position:absolute;top:182px;width:420px;text-align:center}
.col-left{left:160px}
.col-right{left:615px}
.divider{position:absolute;left:600px;top:182px;width:1px;height:550px;background:#555}
.dept{font-size:20px;color:#ccc}
.dept-phone{font-size:28px;font-weight:700;color:#fff;line-height:32px}
.person{font-size:13px;line-height:20px;margin-top:4px}
.person b{color:#fff}
.group{margin-top:28px}
.group .name{color:#fff;font-weight:700;font-size:14px}
.group .rule-sm{width:40px;height:1px;background:#666;margin:0 auto 12px}
.col-right .sub{font-weight:700;color:#fff;font-size:14px;margin:28px 0 16px}
.col-right .person{margin-top:14px}
.base-rule{position:absolute;left:160px;width:880px;top:782px;height:1px;background:#555}
.office{position:absolute;top:825px;left:230px;width:320px;text-align:center;font-size:13px;line-height:20px}
.office b{color:#fff}
.legal{position:absolute;top:825px;left:630px;width:420px;text-align:center}
.legal .person{margin-top:24px}

/* footer */
.site-footer{height:105px;background:var(--black);color:#aaa;font-size:13px;position:relative}
.footer-line{position:absolute;top:22px;left:150px;display:flex;gap:30px}
.footer-line b{color:#fff;font-weight:400}
.footer-line i{font-style:normal;color:#fff}
.footer-po{position:absolute;top:58px;left:150px;font-size:11px;line-height:15px}
.footer-legal{position:absolute;top:58px;right:150px;font-size:11px;line-height:15px;text-align:right}
</style>
</head>
<body>

<header class="site-header">
  <div class="brand"><span class="brand-dot"></span>Kelvar Lease</div>
  <nav class="nav">
    <a class="active" href="#">Home</a>
    <a href="#">About Us</a>
    <a href="#">Rental Programs</a>
    <a href="#">FAQ</a>
    <a href="#">Contact Us</a>
    <a class="btn-login" href="#">Dealer Login</a>
    <a class="btn-pay" href="#">Customer Payments</a>
  </nav>
</header>

<section class="hero" role="img" aria-label="Timber frame of a barn-style storage building under construction against a blue sky">
  <div class="hero-tag">
    <span class="l1">Why pay offsite storage</span><br>
    <span class="l2">when you can rent to own</span>
  </div>
</section>

<section class="welcome">
  <h2 class="title">Welcome to Kelvar Lease</h2>
  <div class="rule"></div>
  <div class="copy">
    <p>Kelvar Lease provides affordable alternatives for your storage needs. Unlike off-site self-storage, Kelvar Lease provides a path to ownership. As an industry leader, we partner with proven, successful storage building retailers and manufacturers to provide quality storage - in your backyard.</p>
    <p>We are pioneers in providing flexible payment options so you can match a rental plan to fit your storage building needs. Ask your retailer about our 24, 36, 48, and 60-month payment options. Why rent self-storage when you can rent then own!</p>
  </div>
</section>

<div class="badge-photo" role="img" aria-label="Round photo of a wooden storage shed with a red roof"></div>

<section class="about">
  <h2 class="title">About Us</h2>
  <div class="rule"></div>
  <div class="copy">
    <p>Kelvar Lease provides affordable alternatives for your storage needs. Unlike off-site self-storage, Kelvar Lease provides a path to ownership. As an industry leader, we partner with proven, successful storage building retailers and manufacturers to provide quality storage - in your backyard.</p>
    <p>We are pioneers in providing flexible payment options so you can match a rental plan to fit your storage building needs. Ask your retailer about our 24, 36, 48, and 60-month payment options. Why rent self-storage when you can rent then own!</p>
  </div>
</section>

<section class="rentals">
  <h2 class="title">Rental Options</h2>
  <div class="rule"></div>
  <div class="terms-label">4 Rental Terms</div>
  <div class="terms">
    <div class="term"><div class="term-ring"><span>24</span></div><div class="term-unit">Months</div></div>
    <div class="term"><div class="term-ring"><span>36</span></div><div class="term-unit">Months</div></div>
    <div class="term"><div class="term-ring"><span>48</span></div><div class="term-unit">Months</div></div>
    <div class="term"><div class="term-ring"><span>60</span></div><div class="term-unit">Months</div></div>
  </div>
  <p>Match the rental plan with the storage building that fits your needs. As a leader in providing creative, affordable storage solutions, Kelvar Lease provides plans that are best suited for you. All Rental Purchase Agreements allow for early payoffs with no penalties. Why rent self-storage? Rent then Own!</p>
</section>

<section class="faq">
  <h2 class="title">Frequently Asked Questions</h2>
  <div class="rule"></div>
  <div class="faq-sub">Common Questions</div>
  <div class="faq-item">
    <h3>Do you require a deposit?</h3>
    <p>Kelvar Lease requires your first and last month's payment prior to delivery of your building. Your last month payment is held in deposit and applied to your last payment in your contract or payoff amount.</p>
  </div>
  <div class="faq-item">
    <h3>When do my payments begin?</h3>
    <p>Your first payment will be due on the 5th of the month following the delivery of the building. The delivery person will provide you with the first payment coupon and you will receive a payment coupon book in the mail to use for all future payments.</p>
  </div>
  <a class="btn-more" href="#">More</a>
</section>

<section class="contact">
  <h2 class="title">Contact Us</h2>
  <div class="rule"></div>

  <div class="col col-left">
    <div class="dept">Dealer Support</div>
    <div class="dept-phone">877-555-0162</div>
    <div class="group">
      <div class="person"><b>Marla</b> – marla@kelvarlease.example ext 2</div>
      <div class="person"><b>Tessa</b> – tessa@kelvarlease.example ext 1</div>
    </div>
    <div class="group"><div class="rule-sm"></div>
      <div class="name">Corwin Beldale</div>
      <div class="person">corwin@kelvarlease.example<br>SC, NC, VA and Eastern TN</div>
    </div>
    <div class="group"><div class="rule-sm"></div>
      <div class="name">Avery Lindqvist</div>
      <div class="person">avery@kelvarlease.example<br>GA, FL, AL</div>
    </div>
    <div class="group"><div class="rule-sm"></div>
      <div class="name">Rusty Ambrose</div>
      <div class="person">rusty@kelvarlease.example<br>MS, LA, AR, Western TN</div>
    </div>
    <div class="group"><div class="rule-sm"></div>
      <div class="name">Glen Harwick</div>
      <div class="person">glen@kelvarlease.example<br>TX, OK</div>
    </div>
  </div>

  <div class="divider"></div>

  <div class="col col-right">
    <div class="dept">Payment Center</div>
    <div class="dept-phone">877-555-0134</div>
    <div class="sub">Account Managers</div>
    <div class="person"><b>Pippa</b> – pippa@kelvarlease.example ext 1</div>
    <div class="person"><b>Nora</b> – nora@kelvarlease.example ext 2</div>
    <div class="person"><b>Wren</b> – wren@kelvarlease.example ext 5</div>
    <div class="person"><b>Sloane</b> – sloane@kelvarlease.example ext 6</div>
    <div class="person"><b>Hollis</b> – hollis@kelvarlease.example ext 3</div>
    <div class="sub">Outside Sales Representative</div>
    <div class="person"><b>Name1</b> – name1@kelvarlease.example ext 1</div>
    <div class="person"><b>Name2</b> – name2@kelvarlease.example ext 2</div>
    <div class="person"><b>Name3</b> – name3@kelvarlease.example ext 5</div>
    <div class="person"><b>Name4</b> – name4@kelvarlease.example ext 6</div>
  </div>

  <div class="base-rule"></div>
  <div class="office">
    <b>Kelvar Lease</b><br>
    P.O. Box 4410<br>
    Millbrook, SC 29000<br>
    Fax Number: 888-555-0199<br>
    Email: info@kelvarlease.example
  </div>
  <div class="legal">
    <div class="dept">Legal Department</div>
    <div class="dept-phone">877-555-0134</div>
    <div class="person"><b>Greta</b> – greta@kelvarlease.example ext 103</div>
  </div>
</section>

<footer class="site-footer">
  <div class="footer-line">
    <span>Main Number: <b>877-555-0160</b></span><i>●</i>
    <span>Payment Center: <b>877-555-0134</b></span><i>●</i>
    <span>Fax Number: <b>888-555-0199</b></span><i>●</i>
    <span>Email: <b>info@kelvarlease.example</b></span>
  </div>
  <div class="footer-po">P.O. Box 4410<br>Millbrook, SC 29000</div>
  <div class="footer-legal">Copyright © 2014 Kelvar Lease. All Rights Reserved<br>Privacy Policy | Terms and Conditions | Refunds</div>
</footer>

</body>
</html>
```